We need a book cover for a novel called "Eleven Lanterns".

In essence it is a novel about a girl, Mira Dunholt, who owns an Antique Shop, The Brass Lantern Emporium, in modern day London. She buys the contents of the deceased estate of Harriet Penrose. Amongst that estate is a box of old English postcards, each postcard providing a snippet of life in London during WWII, all signed by the mysterious "B", and all addressed to "Phil". Whilst Mira is cleaning and pricing some of the belongings from that estate she is unexpectedly transported back in time. She ends up in New Zealand in 1860 at the time of the gold rush; in India in 1856, just as the Indian Revolt occurs; in London in 1896 staying at the Carlmont hotel, and again in London during the Blitz.
This is the Heirloom Hunters Hour woven into the pages of a book as you follow the journey of silver, rubies and diamonds, greenstone and tiger knives (Katar). A novel where tiger hunts and ruby necklaces are entwined with murders and maids.
Each story forms part of the story of Harriet Penrose and the history of her family.
The different stories are magically woven together into a climatic ending, involving auction houses, deadly collectors, and love.

Below is the blurb for the back cover:

"Following the unexplained disappearance of her parents, and in a last ditch attempt to save the antique store she has inherited from financial ruin, Mira Dunholt takes on a deceased estate. Amongst the estate is a collection of fifteen vintage postcards.

Mira is unprepared for the enigma these postcards hint at about their reclusive former owner. They consume her and complicate her life in unimaginable ways.

A novel traversing three continents, and two centuries, where tiger hunts and ruby necklaces are irrevocably entwined with murders and mysteries, auction houses and antiquities.

It might also explain what happened to her parents ..."

This is the Pinterest board with some images on it which capture the essence of the book. http://www.pinboardia.example/tuivdrgr/possible-book-cover-inspirations/

The authors name is Rowena Tallard. Below is the blurb about the author to be included on the back cover:

"Rowena Tallard has worked in her family's antique store since she was a toddler.
She’s gone from being allowed to sell 50c postcards in the corner of Relic Lane, a literal treasure trove, to selling $5,000 Worcester vases at prestigious antique fairs around New Zealand.
She lives in Auckland with her husband and two daughters."

Just added the "blurb" for the back of the book to the brief. Thank you.

Added the Author Blurb to the design brief and a few more images of stamps & postmarks for reference.

Just amended the blurb. Thanks. Last change.

Just updated the blurb and the author's blurb for the back cover in the brief. Please use this latest version. Also loaded an image of the author for the back cover. Please incorporate this in your design for the back cover (not too large though). Thank you so very much.

Target Market(s)

The target reader is a woman, but ideally the cover shouldn't be too feminine.

Industry/Entity Type

Financial

Font styles to use
Script

Requirements
Must have
• Author's name at the bottom, centre. In a plain font.
Nice to have
• A postmark or a stamp or an old postcard/letter image somewhere.
Should not have
• No feather quills.

```html
<!DOCTYPE html>
<html lang="en">
<head>
<meta charset="utf-8">
<title>Eleven Lanterns — Book Cover</title>
<link rel="stylesheet" href="https://fonts.googleapis.com/css2?family=Norican&family=Oranienbaum&family=Oswald:wght@400&display=swap">
<style>
  :root {
    --cover-mid: #58528e;
    --cover-edge: #38335f;
    --cover-deep: #2c284c;
    --title-ink: #ffffff;
    --ruby-light: #ff3a2e;
    --ruby-mid: #d80f0c;
    --ruby-dark: #6e0604;
    --gem-shadow: rgba(28, 24, 52, 0.75);
  }
  html, body {
    margin: 0;
    padding: 0;
    width: 921px;
    height: 1200px;
    overflow: hidden;
    background: var(--cover-deep);
  }
  .book-cover {
    position: relative;
    width: 921px;
    height: 1200px;
    overflow: hidden;
    background:
      radial-gradient(ellipse 70% 60% at 50% 42%, var(--cover-mid) 0%, #4b4680 55%, var(--cover-edge) 100%);
  }
  .cover-texture {
    position: absolute;
    inset: 0;
    background:
      radial-gradient(circle at 22% 18%, rgba(255,255,255,0.05), transparent 30%),
      radial-gradient(circle at 78% 70%, rgba(0,0,0,0.12), transparent 35%),
      radial-gradient(circle at 60% 88%, rgba(0,0,0,0.10), transparent 30%);
  }
  .cover-title {
    position: absolute;
    left: 0;
    right: 0;
    top: 120px;
    margin: 0;
    text-align: center;
    font-family: "Norican", cursive;
    font-weight: 400;
    color: var(--title-ink);
    line-height: 0.82;
    letter-spacing: 1px;
  }
  .cover-title .title-line {
    display: block;
    font-size: 178px;
  }
  .cover-title .title-line--first {
    margin-left: 60px;
  }
  .cover-title .title-line--second {
    margin-left: -10px;
  }
  .cover-tagline {
    position: absolute;
    top: 462px;
    left: 0;
    right: 0;
    margin: 0;
    text-align: center;
    font-family: "Oranienbaum", serif;
    font-size: 26px;
    color: var(--title-ink);
    padding-left: 0;
  }
  .gem-shadow {
    position: absolute;
    left: 235px;
    top: 870px;
    width: 440px;
    height: 80px;
    border-radius: 50%;
    background: radial-gradient(ellipse at center, var(--gem-shadow) 0%, rgba(28,24,52,0.35) 55%, transparent 75%);
  }
  .ruby-art {
    position: absolute;
    left: 200px;
    top: 638px;
    width: 510px;
    height: 290px;
    border-radius: 44% 44% 50% 50% / 30% 30% 70% 70%;
    background: radial-gradient(ellipse at 50% 35%, var(--ruby-light) 0%, var(--ruby-mid) 45%, var(--ruby-dark) 100%);
  }
  .cover-author {
    position: absolute;
    left: 0;
    right: 0;
    bottom: 68px;
    margin: 0;
    text-align: center;
    font-family: "Oranienbaum", serif;
    font-size: 40px;
    color: var(--title-ink);
    letter-spacing: 0.5px;
  }
</style>
</head>
<body>
  <main class="book-cover">
    <div class="cover-texture"></div>
    <h1 class="cover-title">
      <span class="title-line title-line--first">Eleven</span>
      <span class="title-line title-line--second">Lanterns</span>
    </h1>
    <p class="cover-tagline">a novel</p>
    <div class="gem-shadow"></div>
    <div class="ruby-art" role="img" aria-label="Illustration of a large faceted red ruby floating above its shadow"></div>
    <p class="cover-author">Rowena Tallard</p>
  </main>
</body>
</html>
```